Funky new Serviced Apartment Company needs a website + logo

Bright Harbor Serviced Lodging is a new company aiming to attract customers who need temporary accommodation (2 days to 6 months) in city locations.

Our customers make considerable savings on longer stays compared to hotels, and have all the creature comforts of home including super-fast WIFI, comfy beds, full kitchen and modern, yet comfortable, furniture.

Another key feature of the design is a page to attract "Partners" who "Work with Us" by allowing us to manage their properties and becoming part of our network of accommodation units. I have include a brochure from one of our competitors, and a video can be found here: http://lnkshort.example/clipz-7 - both can be used as I have permission.

The website design should work on all devices and screen sizes, and lend itself to a mobile app.

We would like to see website designs that are modern and simple, with a strong brand logo. The final design should communicate "Home From Home" and aim to attract professionals away from home on business for long periods of time.

Target Market(s)

Professional People working away from home for extended periods of time

Industry/Entity Type

Accommodation

Contact Information for Business Card

Name, Title, Phone Number, Email
Malcolm Ostby, Owner, 07831 562087, malcolm.ostby@brightharborsl.co.uk

Logo Text

Bright Harbor Service Lodging (Serviced Accommodation optional)

Coding

Coded - Design and coding required

Number of Pages Required

3 page

Font styles to use
Sans Serif

Requirements
Must have
• A 3 page website: Home, Partners, Contact Us
• Home page should have an area to list current apartment units, the user should be able to select a location and filter the list based on price and number of people.
• Partners page should inspire a "Work with us" call to action.
• The design should work with all screen sizes and devices.
• The design should say friendly and professional
Nice to have
• A simple logo, perhaps a smiling face made up using letters 'W' and 'H'.
• A neutral color scheme
Should not have
• No garish or vivid color scheme

```html
<!DOCTYPE html>
<html lang="en">
<head>
<meta charset="utf-8">
<title>Bright Harbor Serviced Lodging</title>
<link href="https://fonts.googleapis.com/css2?family=Roboto+Condensed:wght@400;700&family=Open+Sans:wght@400;600;700&family=Playfair+Display:wght@700&display=swap" rel="stylesheet">
<style>
:root{
  --ink:#2b2b2b;
  --text:#666;
  --muted:#999;
  --olive:#a9a77c;
  --mauve:#8f7a8c;
  --dark:#2c2c2c;
  --card-dark:#3a3a3a;
  --light:#f1f1f1;
  --line:#dcdcdc;
  --white:#fff;
}
*{margin:0;padding:0;box-sizing:border-box}
html,body{width:1200px;height:3913px;overflow:hidden}
body{font-family:"Open Sans",Arial,sans-serif;color:var(--text);background:var(--white);position:relative}
.cond{font-family:"Roboto Condensed","Arial Narrow",sans-serif}

/* header */
.site-header{position:absolute;top:0;left:0;width:1200px;height:52px;background:var(--white);z-index:5;border-bottom:1px solid #eee}
.brand{position:absolute;left:160px;top:15px;font-family:"Roboto Condensed",sans-serif;font-weight:700;font-size:19px;color:var(--ink);letter-spacing:.5px}
.main-nav{position:absolute;right:160px;top:19px;display:flex;gap:30px;font-family:"Roboto Condensed",sans-serif;font-size:12px;color:var(--ink)}

/* hero */
.hero{position:absolute;top:52px;left:0;width:1200px;height:457px}
.hero-photo{position:absolute;inset:0;background:linear-gradient(180deg,#6e6a68 0%,#8c8886 45%,#a7a3a0 75%,#cfcbc6 100%)}
.hero-content{position:absolute;top:175px;left:0;width:1200px;text-align:center;color:var(--white)}
.hero-title{font-family:"Roboto Condensed",sans-serif;font-weight:700;font-size:34px;letter-spacing:-.5px;text-transform:uppercase;text-shadow:0 1px 3px rgba(0,0,0,.3)}
.hero-text{width:560px;margin:8px auto 0;font-size:13px;line-height:19px}
.btn-outline{display:inline-flex;align-items:center;gap:6px;border:1.5px solid var(--white);color:var(--white);font-family:"Roboto Condensed",sans-serif;font-weight:700;font-size:12px;padding:8px 16px;text-transform:uppercase}
.hero .btn-outline{margin-top:38px}
.btn-outline svg{width:11px;height:11px}

/* welcome */
.welcome{position:absolute;top:509px;left:0;width:1200px;height:456px;text-align:center}
.welcome-bg-word{position:absolute;top:30px;left:0;width:1200px;font-family:"Playfair Display",serif;font-size:110px;color:#f3f3f3;letter-spacing:4px;line-height:1}
.welcome-title{position:relative;margin-top:62px;font-family:"Playfair Display",serif;font-weight:700;font-size:36px;color:var(--ink);letter-spacing:1px}
.welcome-tag{position:relative;font-size:9px;letter-spacing:1.5px;color:var(--muted);margin-top:2px}
.welcome-rule{position:relative;margin:6px auto 0;width:120px;height:10px}
.welcome-lead{position:relative;margin-top:40px;font-family:"Roboto Condensed",sans-serif;font-weight:700;font-size:15px;color:var(--ink)}
.welcome-copy{position:relative;width:880px;margin:20px auto 0;font-size:11px;line-height:17px;color:var(--text)}
.amenities{position:absolute;top:326px;left:160px;width:880px;display:flex}
.amenity{flex:1;text-align:center;border-left:1px solid var(--line);height:92px;padding-top:8px}
.amenity:first-child{border-left:none}
.amenity svg{width:52px;height:48px;stroke:#777;fill:none;stroke-width:2}
.amenity span{display:block;margin-top:8px;font-family:"Roboto Condensed",sans-serif;font-size:14px;color:#555;text-transform:uppercase}

/* split bands */
.split{position:absolute;left:0;width:1200px;height:363px;display:flex}
.what-we-do{top:973px;height:360px}
.work-with-us{top:1333px}
.split-photo{width:569px;height:100%}
.split-panel{width:631px;height:100%;padding:32px 42px 0 44px;color:var(--white)}
.work-with-us .split-panel{width:569px;padding:36px 40px 0 156px}
.work-with-us .split-photo{width:631px}
.panel-olive{background:var(--olive)}
.panel-mauve{background:var(--mauve)}
.split-title{font-family:"Roboto Condensed",sans-serif;font-weight:700;font-size:31px;text-transform:uppercase}
.split-rule{width:46px;height:2px;background:var(--white);margin:4px 0 16px}
.split-copy{font-size:10.5px;line-height:15.5px;margin-bottom:12px}
.split-panel .btn-outline{margin-top:8px;padding:7px 12px;font-size:11px}

/* benefits */
.benefits{position:absolute;top:1696px;left:0;width:1200px;height:511px;text-align:center}
.section-title{font-family:"Roboto Condensed",sans-serif;font-weight:700;font-size:31px;color:var(--ink);text-transform:uppercase}
.benefits .section-title{margin-top:44px}
.title-rule{width:60px;height:2px;background:var(--olive);margin:6px auto 0}
.benefits-copy{width:760px;margin:14px auto 0;font-size:11px;line-height:18px;color:var(--muted)}
.video{position:absolute;top:172px;left:162px;width:425px;height:277px;background:linear-gradient(180deg,#8a8c90 0%,#5c5f63 55%,#4a4038 80%,#6b7b84 100%)}
.play{position:absolute;left:178px;top:105px;width:66px;height:66px}
.accordion{position:absolute;top:172px;left:605px;width:433px;text-align:left;border:1px solid #e5e5e5}
.acc-item{border-top:1px solid #e5e5e5;height:40px;display:flex;align-items:center;padding:0 14px;font-family:"Roboto Condensed",sans-serif;font-weight:700;font-size:11px;color:var(--ink);text-transform:uppercase;position:relative}
.acc-item:first-child{border-top:none}
.acc-item svg.ic{width:18px;height:18px;margin-right:10px;stroke:#777;fill:none;stroke-width:1.6}
.acc-item svg.chev{position:absolute;right:14px;width:14px;height:10px;stroke:#999;fill:none;stroke-width:1.5}
.acc-body{border-top:1px solid #e5e5e5;height:150px;padding:16px 34px 0 18px;font-size:9.5px;line-height:15px;color:var(--muted);font-style:italic;position:relative}
.acc-body::after{content:"";position:absolute;right:12px;top:16px;width:3px;height:70px;background:#bbb}
.acc-item.open{background:#fafafa}

/* gallery */
.gallery{position:absolute;top:2207px;left:0;width:1200px;height:553px}
.tile{position:absolute}
.tile-caption{position:absolute;left:46px;top:30px;color:var(--white)}
.tile-caption b{display:block;font-family:"Roboto Condensed",sans-serif;font-size:22px;font-weight:700}
.tile-caption span{font-size:10px;border-bottom:2px solid var(--olive);padding-bottom:2px}

/* listings */
.listings{position:absolute;top:2760px;left:0;width:1200px;height:587px;text-align:center}
.title-lines{display:flex;align-items:center;justify-content:center;gap:24px;margin-top:50px}
.title-lines i{display:block;width:170px;border-top:1px solid #bbb;border-bottom:1px solid #bbb;height:4px}
.cards{position:absolute;top:128px;left:162px;display:flex;gap:26px}
.card{width:276px;height:399px;background:#f0f0f0;position:relative}
.card-photo{height:172px}
.price-bar{height:36px;background:var(--mauve);color:var(--white);display:flex;align-items:center;justify-content:space-between;padding:0 12px;font-size:10px}
.price-bar b{font-size:11px}
.price-bar span{display:flex;align-items:center;gap:6px}
.card h3{font-family:"Roboto Condensed",sans-serif;font-size:14px;color:var(--ink);margin-top:22px}
.card p{font-size:10.5px;line-height:16px;color:var(--text);padding:10px 22px 0}
.card-foot{position:absolute;bottom:0;left:0;width:100%;height:36px;background:var(--card-dark);color:#ddd;display:flex;justify-content:space-around;align-items:center;font-size:10px}
.card-foot span{display:flex;align-items:center;gap:5px}
.card-foot svg{width:14px;height:12px;fill:#ccc}

/* partners */
.partners{position:absolute;top:3347px;left:0;width:1200px;height:196px;background:var(--light);text-align:center}
.partners .title-lines{margin-top:30px}
.partners .section-title{font-size:24px}
.partner-row{position:absolute;top:89px;left:180px;width:840px;display:flex;gap:20px;justify-content:center}
.partner{width:152px;height:84px;background:var(--white);display:flex;align-items:center;justify-content:center}
.partner i{display:block;width:46px;height:46px;background:#d7d7d7}
.partner i.round{border-radius:50%}
.arrow{position:absolute;top:124px;width:30px;height:30px;background:#555;transform:rotate(45deg)}
.arrow svg{transform:rotate(-45deg);width:30px;height:30px}
.arrow.prev{left:96px}
.arrow.next{left:1049px}

/* footer */
.site-footer{position:absolute;top:3543px;left:0;width:1200px;height:370px;background:linear-gradient(180deg,#353433,#242424);text-align:center;color:#aaa}
.subscribe{position:absolute;top:65px;left:360px;width:448px;height:34px;display:flex}
.subscribe .field{flex:1;background:var(--white);display:flex;align-items:center;padding-left:12px;font-size:10px;color:var(--muted);gap:8px}
.subscribe .go{width:108px;background:var(--mauve);color:var(--white);font-family:"Roboto Condensed",sans-serif;font-weight:700;font-size:12px;display:flex;align-items:center;justify-content:center;text-transform:uppercase}
.footer-brand{position:absolute;top:130px;width:100%;font-family:"Roboto Condensed",sans-serif;font-weight:700;font-size:26px;color:var(--olive)}
.footer-rule{position:absolute;top:168px;left:570px;width:60px;height:2px;background:var(--olive)}
.footer-copy{position:absolute;top:188px;left:240px;width:720px;font-size:10px;line-height:17px;color:#999}
.socials{position:absolute;top:260px;left:0;width:100%;display:flex;justify-content:center;gap:14px}
.socials i{display:block;width:26px;height:26px;border:1.5px solid #888;border-radius:50%}
.contact-row{position:absolute;top:322px;left:0;width:100%;display:flex;justify-content:center;gap:34px;font-size:10px;color:#aaa}
.contact-row span{display:flex;align-items:center;gap:6px}
.contact-row svg{width:11px;height:11px;fill:#aaa}
</style>
</head>
<body>

<header class="site-header">
  <div class="brand">BRIGHT HARBOR</div>
  <nav class="main-nav"><span>HOME</span><span>PARTNERS</span><span>CONTACT US</span></nav>
</header>

<section class="hero">
  <div class="hero-photo" role="img" aria-label="Modern grey living room with a dark sofa, side tables and floor lamp"></div>
  <div class="hero-content">
    <h1 class="hero-title">The Highest Class Comfort Home Accommodation</h1>
    <p class="hero-text">Serviced homes for professionals on long stays, with full kitchens, fast wifi and comfortable beds in the heart of the city.</p>
    <span class="btn-outline">Read More <svg viewBox="0 0 12 12"><circle cx="6" cy="6" r="5.5" fill="#fff"/><path d="M5 3.5 7.5 6 5 8.5" stroke="#777" stroke-width="1.4" fill="none"/></svg></span>
  </div>
</section>

<section class="welcome">
  <div class="welcome-bg-word">WELCOME</div>
  <h2 class="welcome-title">BRIGHT HARBOR</h2>
  <div class="welcome-tag">ONE OF THE BEST PLACES TO RELAX &amp; ENJOY</div>
  <svg class="welcome-rule" viewBox="0 0 120 10"><path d="M0 5H52M68 5H120" stroke="#888" stroke-width="1"/><path d="M60 1 64 5 60 9 56 5Z" fill="#666"/></svg>
  <div class="welcome-lead">PROVIDING QUALITY HOME ACCOMMODATION SERVICES SINCE '98</div>
  <p class="welcome-copy">We look after professionals who spend weeks or months away from home for work. Every apartment is fully furnished and cleaned each week, with a full kitchen, fast wifi, fresh linen and a comfortable bed ready on arrival. Our homes sit close to transport links and business districts, and long stays cost far less than a hotel, so you can settle in, cook your own meals and truly feel at home while you work in the city.</p>
  <div class="amenities">
    <div class="amenity"><svg viewBox="0 0 52 48"><path d="M10 14h32v6H10z"/><path d="M18 14V8h16v6"/><path d="M8 40h36M14 20v20M38 20v20"/></svg><span>Kitchen</span></div>
    <div class="amenity"><svg viewBox="0 0 52 48"><path d="M8 42V6h36v36"/><path d="M8 6l16 8v28M44 6 28 14v28"/></svg><span>Room</span></div>
    <div class="amenity"><svg viewBox="0 0 52 48"><path d="M6 38V14h40v24M6 30h40"/><rect x="11" y="20" width="12" height="8" rx="2"/><rect x="29" y="20" width="12" height="8" rx="2"/></svg><span>Bedrooms</span></div>
    <div class="amenity"><svg viewBox="0 0 52 48"><path d="M4 24h44v6a10 10 0 0 1-10 10H14A10 10 0 0 1 4 30z"/><path d="M12 24V10a4 4 0 0 1 8 0M14 40l-2 4M38 40l2 4"/></svg><span>Bathrooms</span></div>
    <div class="amenity"><svg viewBox="0 0 52 48"><path d="M8 36V18a4 4 0 0 1 4-4h28a4 4 0 0 1 4 4v18z"/><path d="M4 24h8v12M48 24h-8v12M12 28h28M10 36v4M42 36v4"/></svg><span>Living Rooms</span></div>
    <div class="amenity"><svg viewBox="0 0 52 48"><circle cx="26" cy="14" r="3"/><path d="M26 17v26M20 43h12M18 8a11 11 0 0 0 0 12M34 8a11 11 0 0 1 0 12M13 4a17 17 0 0 0 0 20M39 4a17 17 0 0 1 0 20"/></svg><span>Wifi</span></div>
  </div>
</section>

<section class="split what-we-do">
  <div class="split-photo" role="img" aria-label="Bright white kitchen with a dark worktop island and pendant lights" style="background:linear-gradient(135deg,#e9e4d9 0%,#c9b79a 40%,#8a6a4a 70%,#3a2e26 100%)"></div>
  <div class="split-panel panel-olive">
    <h2 class="split-title">What We Do</h2>
    <div class="split-rule"></div>
    <p class="split-copy">We find, furnish and run quality apartments in central city locations for guests who need a home for a few days or a few months. Each unit is prepared to a hotel standard of cleanliness but keeps the space, privacy and warmth of a real home, so guests can unpack properly and live normally during their stay.</p>
    <p class="split-copy">Our team handles bookings, check-in, cleaning, maintenance and support around the clock. Companies can book single stays or ongoing allocations for staff, with clear monthly invoicing, flexible dates and a single point of contact who knows every property and every guest by name.</p>
    <span class="btn-outline">Read More <svg viewBox="0 0 12 12"><circle cx="6" cy="6" r="5.5" fill="#fff"/><path d="M5 3.5 7.5 6 5 8.5" stroke="#a9a77c" stroke-width="1.4" fill="none"/></svg></span>
  </div>
</section>

<section class="split work-with-us">
  <div class="split-panel panel-mauve">
    <h2 class="split-title">Work With Us</h2>
    <div class="split-rule"></div>
    <p class="split-copy">Own a flat in the city? Let us manage it for you and join our growing network of serviced homes. We take care of guests, cleaning, repairs and bookings, while you receive steady income without the daily work of letting.</p>
    <p class="split-copy">Our partners enjoy fewer empty weeks, careful guests from trusted companies and clear monthly reports. We prepare your property to our standard, list it across our channels and keep it in top condition all year round.</p>
    <span class="btn-outline">Read More <svg viewBox="0 0 12 12"><circle cx="6" cy="6" r="5.5" fill="#fff"/><path d="M5 3.5 7.5 6 5 8.5" stroke="#8f7a8c" stroke-width="1.4" fill="none"/></svg></span>
  </div>
  <div class="split-photo" role="img" aria-label="Two people in business suits shaking hands" style="background:linear-gradient(120deg,#d9dfe6 0%,#a9b6c4 40%,#6d7f92 65%,#2b3440 100%)"></div>
</section>

<section class="benefits">
  <h2 class="section-title">Benefits of Bright Harbor</h2>
  <div class="title-rule"></div>
  <p class="benefits-copy">I have worked in property management for over fourteen years, mostly around the Ashford region. Now working with homes across the city, I bring the care of a small host with the reliability of a full professional service at a fair price.</p>
  <div class="video" role="img" aria-label="Modern two-storey house at dusk with lit windows and a pool">
    <svg class="play" viewBox="0 0 66 66"><circle cx="33" cy="33" r="31" fill="rgba(255,255,255,.35)" stroke="#fff" stroke-width="2"/><path d="M27 21 45 33 27 45Z" fill="#fff"/></svg>
  </div>
  <div class="accordion">
    <div class="acc-item open"><svg class="ic" viewBox="0 0 18 18"><path d="M3 4h12v10H3zM6 8h6M6 11h4"/></svg>Being a Bright Harbor partner provides you with<svg class="chev" viewBox="0 0 14 10"><path d="M2 7l5-5 5 5"/></svg></div>
    <div class="acc-body">Reliable monthly income, fewer empty nights and careful guests from trusted companies. We handle every booking, clean, repair and question, and send you a clear report each month so you always know how your property is doing and what it has earned for you. Your home is looked after as if it were ours.</div>
    <div class="acc-item"><svg class="ic" viewBox="0 0 18 18"><path d="M4 2v14M9 2v14M14 2v14M2 6h4M7 11h4M12 7h4"/></svg>We make your life easier...<svg class="chev" viewBox="0 0 14 10"><path d="M2 3l5 5 5-5"/></svg></div>
    <div class="acc-item"><svg class="ic" viewBox="0 0 18 18"><circle cx="9" cy="9" r="7"/><circle cx="9" cy="9" r="3"/></svg>...so you can enjoy the benefits<svg class="chev" viewBox="0 0 14 10"><path d="M2 3l5 5 5-5"/></svg></div>
  </div>
</section>

<section class="gallery">
  <div class="tile" role="img" aria-label="Bedroom with a large bed, teal throw and pillows" style="left:0;top:0;width:595px;height:277px;background:linear-gradient(180deg,#9a9b98 0%,#6e7472 50%,#3e5654 100%)">
    <div class="tile-caption"><b>Luxury Comfort Bed</b><span>Home / Accommodation</span></div>
  </div>
  <div class="tile" role="img" aria-label="Open kitchen with white island and wooden floor" style="left:595px;top:0;width:305px;height:277px;background:linear-gradient(180deg,#eeeeec 0%,#c9c4bb 55%,#6e5a46 100%)"></div>
  <div class="tile" role="img" aria-label="Grey lounge with a dark sofa and red cushions" style="left:900px;top:0;width:300px;height:277px;background:linear-gradient(180deg,#b7b5b2 0%,#8d8b88 60%,#3c3b3a 100%)"></div>
  <div class="tile" role="img" aria-label="Yellow and grey seating area with black chairs" style="left:0;top:277px;width:298px;height:276px;background:linear-gradient(135deg,#d7c63a 0%,#9d9a6c 45%,#3a3a3a 100%)"></div>
  <div class="tile" role="img" aria-label="Purple lit bedroom with table lamp and vases" style="left:298px;top:277px;width:299px;height:276px;background:linear-gradient(135deg,#c9c2cf 0%,#6e5e78 45%,#2a2430 100%)"></div>
  <div class="tile" role="img" aria-label="Dark kitchen with wooden worktop and built-in oven" style="left:597px;top:277px;width:603px;height:276px;background:linear-gradient(180deg,#2a2626 0%,#6b4a34 45%,#d9d4c9 75%,#bfb8ab 100%)"></div>
</section>

<section class="listings">
  <div class="title-lines"><i></i><h2 class="section-title">List Current Apartment</h2><i></i></div>
  <div class="cards">
    <article class="card">
      <div class="card-photo" role="img" aria-label="Brick apartment building with balconies" style="background:linear-gradient(180deg,#9cc3e3 0%,#b9845e 55%,#7a5a40 100%)"></div>
      <div class="price-bar"><span><svg width="9" height="12" viewBox="0 0 9 12"><path d="M4.5 0A4.5 4.5 0 0 0 0 4.5C0 8 4.5 12 4.5 12S9 8 9 4.5A4.5 4.5 0 0 0 4.5 0Zm0 6.3a1.8 1.8 0 1 1 0-3.6 1.8 1.8 0 0 1 0 3.6Z" fill="#fff"/></svg>Riverside Quarter, City Centre</span><b>$479,000</b></div>
      <h3>Cozy apartment in Silverado</h3>
      <p>Bright two bedroom flat close to shops and transport, with a full kitchen and fast wifi throughout.</p>
      <div class="card-foot"><span><svg viewBox="0 0 14 12"><path d="M0 12V3h2v5h12v4h-2v-2H2v2zM3 4h4v3H3zM8 4h6v3H8z"/></svg>2 bedrooms</span><span><svg viewBox="0 0 14 12"><path d="M0 6h14v2a4 4 0 0 1-4 4H4a4 4 0 0 1-4-4zM2 6V1h3v1H3v4z"/></svg>3 baths</span><span><svg viewBox="0 0 14 12"><circle cx="7" cy="3" r="3"/><path d="M1 12a6 5 0 0 1 12 0z"/></svg>12</span></div>
    </article>
    <article class="card">
      <div class="card-photo" role="img" aria-label="Red and white apartment block against blue sky" style="background:linear-gradient(180deg,#8fc0e8 0%,#c9a894 50%,#a4543a 100%)"></div>
      <div class="price-bar"><span><svg width="9" height="12" viewBox="0 0 9 12"><path d="M4.5 0A4.5 4.5 0 0 0 0 4.5C0 8 4.5 12 4.5 12S9 8 9 4.5A4.5 4.5 0 0 0 4.5 0Zm0 6.3a1.8 1.8 0 1 1 0-3.6 1.8 1.8 0 0 1 0 3.6Z" fill="#fff"/></svg>Old Market Square, East Side</span><b>$479,000</b></div>
      <h3>Cozy apartment in Silverado</h3>
      <p>Quiet corner flat with large windows, a modern lounge and a short walk to the business district.</p>
      <div class="card-foot"><span><svg viewBox="0 0 14 12"><path d="M0 12V3h2v5h12v4h-2v-2H2v2zM3 4h4v3H3zM8 4h6v3H8z"/></svg>2 bedrooms</span><span><svg viewBox="0 0 14 12"><path d="M0 6h14v2a4 4 0 0 1-4 4H4a4 4 0 0 1-4-4zM2 6V1h3v1H3v4z"/></svg>4 baths</span><span><svg viewBox="0 0 14 12"><circle cx="7" cy="3" r="3"/><path d="M1 12a6 5 0 0 1 12 0z"/></svg>17</span></div>
    </article>
    <article class="card">
      <div class="card-photo" role="img" aria-label="Tall modern residential tower with blue sky" style="background:linear-gradient(180deg,#5f9fd8 0%,#a9c5de 50%,#8c8f94 100%)"></div>
      <div class="price-bar"><span><svg width="9" height="12" viewBox="0 0 9 12"><path d="M4.5 0A4.5 4.5 0 0 0 0 4.5C0 8 4.5 12 4.5 12S9 8 9 4.5A4.5 4.5 0 0 0 4.5 0Zm0 6.3a1.8 1.8 0 1 1 0-3.6 1.8 1.8 0 0 1 0 3.6Z" fill="#fff"/></svg>Harbour Walk, Waterfront</span><b>$479,000</b></div>
      <h3>Cozy apartment in Silverado</h3>
      <p>Spacious home near the river with a balcony, comfy beds and parking for longer business stays.</p>
      <div class="card-foot"><span><svg viewBox="0 0 14 12"><path d="M0 12V3h2v5h12v4h-2v-2H2v2zM3 4h4v3H3zM8 4h6v3H8z"/></svg>2 bedrooms</span><span><svg viewBox="0 0 14 12"><path d="M0 6h14v2a4 4 0 0 1-4 4H4a4 4 0 0 1-4-4zM2 6V1h3v1H3v4z"/></svg>2 baths</span><span><svg viewBox="0 0 14 12"><circle cx="7" cy="3" r="3"/><path d="M1 12a6 5 0 0 1 12 0z"/></svg>15</span></div>
    </article>
  </div>
</section>

<section class="partners">
  <div class="title-lines"><i></i><h2 class="section-title">Our Partners</h2><i></i></div>
  <div class="arrow prev"><svg viewBox="0 0 30 30"><path d="M17 10l-5 5 5 5" stroke="#fff" stroke-width="2" fill="none"/></svg></div>
  <div class="partner-row">
    <div class="partner"><i></i></div>
    <div class="partner"><i class="round"></i></div>
    <div class="partner"><i></i></div>
    <div class="partner"><i class="round"></i></div>
    <div class="partner"><i></i></div>
  </div>
  <div class="arrow next"><svg viewBox="0 0 30 30"><path d="M13 10l5 5-5 5" stroke="#fff" stroke-width="2" fill="none"/></svg></div>
</section>

<footer class="site-footer">
  <div class="subscribe">
    <div class="field"><svg width="11" height="9" viewBox="0 0 11 9"><path d="M0 0h11v9H0z" fill="#aaa"/><path d="M0 0l5.5 5L11 0" stroke="#fff" fill="none"/></svg>Enter Your Email Id</div>
    <div class="go">Subscribe</div>
  </div>
  <div class="footer-brand">BRIGHT HARBOR</div>
  <div class="footer-rule"></div>
  <p class="footer-copy">Serviced homes for people who work away from home. Flexible stays from two days to six months, fully furnished apartments, weekly cleaning and friendly support whenever you need it, all across the city.</p>
  <div class="socials"><i></i><i></i><i></i></div>
  <div class="contact-row">
    <span><svg viewBox="0 0 9 12"><path d="M4.5 0A4.5 4.5 0 0 0 0 4.5C0 8 4.5 12 4.5 12S9 8 9 4.5A4.5 4.5 0 0 0 4.5 0Z"/></svg>48 Quay Street, Fairview, London</span>
    <span><svg viewBox="0 0 11 9"><path d="M0 0h11v9H0z"/></svg>hello@brightharborsl.example</span>
    <span><svg viewBox="0 0 12 12"><path d="M2 0h3l1 3-2 1a7 7 0 0 0 4 4l1-2 3 1v3a2 2 0 0 1-2 2A10 10 0 0 1 0 2a2 2 0 0 1 2-2Z"/></svg>(+44) 20 7946 0321</span>
  </div>
</footer>

</body>
</html>
```